Swimming Pool Supply Company Business Cards

We need business cards designed for company. These need to be easy to edit so that we can fill in names, titles, and contact info for each person who works here.

Dalton R. Whitfield
Manager of Legal & Finance
K.L. Brisbane, Incorporated

4837 Grenway Avenue
Marlow Heights, PA 19243

E. dalton@klbrisbane-example.com
M. (215) 555-0173
O. (215) 555-0148

Contact Information for Business Card

Looking to upgrade current business cards with graphic that can be edited. Looking for fresh ideas for an age old industry.

Font styles to use
Serif
Sans Serif

Colors

Designer to choose colors to be used in the design.

Requirements
Must have
• Professional, fresh, unique but professional

```html
<!DOCTYPE html>
<html lang="en">
<head>
<meta charset="utf-8">
<title>K.L. Brisbane Business Cards</title>
<link href="https://fonts.googleapis.com/css2?family=Lato:wght@400;700;900&display=swap" rel="stylesheet">
<style>
  :root {
    --backdrop: #1c1c1e;
    --card-black: #1f1f1f;
    --panel-dark: #141414;
    --panel-mid: #2e2e2e;
    --paper: #ffffff;
    --ink: #222222;
    --ink-soft: #444444;
    --light: #f2f2f2;
  }
  * { margin: 0; padding: 0; box-sizing: border-box; }
  html, body {
    width: 1200px; height: 912px; overflow: hidden;
    background: var(--backdrop);
    font-family: "Lato", Arial, sans-serif;
  }
  .card {
    position: absolute;
    width: 700px; height: 400px;
    box-shadow: 0 18px 40px rgba(0,0,0,0.6);
    overflow: hidden;
  }
  /* Front */
  .card-front {
    left: 110px; top: 50px;
    background: var(--card-black);
    color: var(--light);
  }
  .front-brand {
    position: absolute; left: 0; right: 0; top: 120px;
    text-align: center;
  }
  .brand-name {
    font-weight: 900;
    font-size: 84px;
    letter-spacing: 2px;
    line-height: 1;
    text-transform: uppercase;
  }
  .brand-tagline {
    font-size: 19px;
    margin-top: 10px;
  }
  .front-web {
    position: absolute; left: 0; right: 0; bottom: 60px;
    text-align: center; font-size: 17px;
  }
  /* Back */
  .card-back {
    left: 390px; top: 470px;
    background: var(--paper);
    display: flex;
  }
  .back-info {
    width: 400px; padding: 40px 0 0 36px;
    color: var(--ink);
  }
  .back-info .brand-name { font-size: 66px; color: var(--ink); }
  .back-info .brand-tagline { font-size: 15px; margin-top: 6px; color: var(--ink); }
  .address {
    margin-top: 40px; font-size: 19px; line-height: 1.25; color: var(--ink-soft);
  }
  .contact-list { list-style: none; margin-top: 14px; }
  .contact-list li {
    display: flex; align-items: center; gap: 14px;
    font-size: 19px; line-height: 1.3; color: var(--ink-soft);
  }
  .contact-list svg { width: 16px; height: 16px; flex: none; }
  .back-panel {
    position: relative; flex: 1;
    background: linear-gradient(160deg, var(--panel-dark) 0%, var(--panel-mid) 55%, var(--panel-dark) 100%);
    color: var(--light);
    padding: 50px 0 0 26px;
  }
  .person-name { font-size: 26px; font-weight: 700; }
  .person-title { font-size: 16px; margin-top: 4px; }
  .edge-strip {
    position: absolute; top: 0; right: 0; width: 50px; height: 100%;
    background: var(--paper);
  }
  .edge-strip::before, .edge-strip::after {
    content: ""; position: absolute; top: 0; height: 100%; width: 3px;
    background: var(--panel-dark);
  }
  .edge-strip::before { left: 10px; }
  .edge-strip::after { left: 20px; }
</style>
</head>
<body>

<section class="card card-front">
  <div class="front-brand">
    <div class="brand-name">Brisbane</div>
    <div class="brand-tagline">Big Enough to Serve You, Small Enough to Care</div>
  </div>
  <div class="front-web">www.klbrisbane-example.com</div>
</section>

<section class="card card-back">
  <div class="back-info">
    <div class="brand-name">Brisbane</div>
    <div class="brand-tagline">Big Enough to Serve You, Small Enough to Care</div>
    <p class="address">K.L. Brisbane, Incorporated<br>4837 Grenway Avenue<br>Marlow Heights, PA 19243</p>
    <ul class="contact-list">
      <li>
        <svg viewBox="0 0 16 16" aria-hidden="true"><path d="M3 1l3 3-1.5 2a9 9 0 0 0 5.5 5.5L12 10l3 3-2 2C7 15 1 9 1 3z" fill="#333"/></svg>
        (215) 555-0148
      </li>
      <li>
        <svg viewBox="0 0 16 16" aria-hidden="true"><rect x="4" y="1" width="8" height="14" rx="1.5" fill="none" stroke="#333" stroke-width="1.5"/><rect x="6" y="3" width="4" height="6" fill="#333"/></svg>
        (215) 555-0173
      </li>
      <li>
        <svg viewBox="0 0 16 16" aria-hidden="true"><rect x="1" y="3" width="14" height="10" fill="#333"/><path d="M1 3l7 6 7-6" fill="none" stroke="#fff" stroke-width="1.2"/></svg>
        dalton@klbrisbane-example.com
      </li>
      <li>
        <svg viewBox="0 0 16 16" aria-hidden="true"><circle cx="8" cy="8" r="7" fill="#333"/><path d="M1 8h14M8 1c-3 3-3 11 0 14M8 1c3 3 3 11 0 14" fill="none" stroke="#fff" stroke-width="0.9"/></svg>
        www.klbrisbane-example.com
      </li>
    </ul>
  </div>
  <div class="back-panel">
    <div class="person-name">Dalton R. Whitfield</div>
    <div class="person-title">Manager of Legal &amp; Finance</div>
    <div class="edge-strip"></div>
  </div>
</section>

</body>
</html>
```